Adapt logo for box truck wrap for my restoration company

I need a wrap for our company Brightway Restoration. We specialize in water damage restoration. I’ve attached our logo, business card, and page header. Things I would like to include are- 24 hour emergency service, our phone number (555)014-7392 and that we do water, fire and mold work. It’s a 2004 Kardella Vonter which I’ve attached pictures of. I will get the cab wrapped as well.

Industry/Entity Type

Construction- specifically Restoration

Font styles to use
Sans Serif

Colors

Designer to choose colors to be used in the design.

Requirements
Must have
• Water• Fire• Mold, phone number (555)014-7392
Nice to have
• Clean, professional look with the logo

```html
<!DOCTYPE html>
<html lang="en">
<head>
<meta charset="utf-8">
<title>Brightway Restoration – Box Truck Side Wrap</title>
<link rel="stylesheet" href="https://fonts.googleapis.com/css2?family=Bebas+Neue&display=swap">
<style>
  :root {
    --brand-blue: #138ee3;
    --brand-grey: #858585;
    --panel-white: #ffffff;
    --page-bg: #eef1f4;
    --panel-edge: #d6dade;
  }
  html, body {
    margin: 0;
    padding: 0;
    width: 1200px;
    height: 1000px;
    overflow: hidden;
    background: var(--page-bg);
  }
  .canvas {
    position: relative;
    width: 1200px;
    height: 1000px;
    display: flex;
    align-items: center;
    justify-content: center;
  }
  .wrap-panel {
    width: 1160px;
    height: 586px;
    display: block;
    box-shadow: 0 0 0 1px var(--panel-edge);
    background: var(--panel-white);
  }
  .wrap-text {
    font-family: "Bebas Neue", "Oswald", sans-serif;
  }
  .fill-blue { fill: var(--brand-blue); }
  .fill-grey { fill: var(--brand-grey); }
  .fill-white { fill: var(--panel-white); }
</style>
</head>
<body>
<main class="canvas">
  <svg class="wrap-panel" viewBox="0 0 1495 755" xmlns="http://www.w3.org/2000/svg" aria-label="Brightway Restoration box truck side wrap">
    <rect class="fill-white" x="0" y="0" width="1495" height="755"/>

    <!-- plain accent bands -->
    <g class="accent-band-top">
      <rect class="fill-blue" x="630" y="0" width="865" height="26"/>
      <rect class="fill-grey" x="1010" y="34" width="485" height="12"/>
    </g>
    <g class="accent-band-bottom">
      <rect class="fill-grey" x="0" y="709" width="360" height="12"/>
      <rect class="fill-blue" x="0" y="729" width="740" height="26"/>
    </g>

    <!-- brand name mark -->
    <g class="brand-mark">
      <circle class="fill-grey" cx="175" cy="375" r="48"/>
      <text class="wrap-text fill-blue" x="245" y="415" font-size="118" textLength="360" lengthAdjust="spacingAndGlyphs">BRIGHTWAY</text>
    </g>

    <!-- headline and service details -->
    <text class="wrap-text fill-blue company-name" x="627" y="312" font-size="148" textLength="750" lengthAdjust="spacingAndGlyphs">BRIGHTWAY RESTORATION</text>
    <text class="wrap-text fill-grey service-hours" x="770" y="421" font-size="106" textLength="465" lengthAdjust="spacingAndGlyphs">24 HOUR SERVICE</text>
    <text class="wrap-text fill-blue phone-number" x="775" y="531" font-size="114" textLength="458" lengthAdjust="spacingAndGlyphs">555-014-7392</text>
    <text class="wrap-text fill-grey service-list" x="770" y="621" font-size="86" textLength="467" lengthAdjust="spacingAndGlyphs">WATER • FIRE • MOLD</text>
  </svg>
</main>
</body>
</html>
```